Business Card Design for BrightwaveOutreach.com

--I need a business card design for my company BrightwaveOutreach.com

I have attached my logo...I want the brightwave outreach logo on the front of the business card, and then I want The Brightwave Chief on the back of it with my information.

I would like to see a light colored background as well as a dark colored background

FRONT:
BRIGHTWAVE OUTREACH LOGO
482 N. Elmwood
3rd Floor
San Diego CA 92101
www.BrightwaveOutreach.com

Advanced Website & App Development
Websites, Apps, Online Voucher Systems

Leading Edge Marketing Services
SMS, VB, SMM, SEM,

BACK:
BRIGHTWAVE CHIEF LOGO
Dorian Pelley
The Brightwave Chief
Call Or Text: 619-555-0148
Dorian@BrightwaveChief.com
www.BrightwaveChief.com

Target Market(s)

small business owners

Industry/Entity Type

Business Consultant

Contact Information for Business Card

FRONT:
BRIGHTWAVE OUTREACH LOGO
482 N. Elmwood
3rd Floor
San Diego CA 92101
www.BrightwaveOutreach.com

SMS, VB, SMM, SEM,

BACK:
BRIGHTWAVE CHIEF LOGO
Dorian Pelley
The Brightwave Chief
Dorian@BrightwaveChief.com
www.BrightwaveChief.com

Requirements
Must have
• add this quote on it somewhere, anywhere,preferrably on back
• "The Fastest Way To Success Is To Take Action”
• — Dorian Pelley, Brightwave Chief
Nice to have
• open
Should not have
• red

```html
<!DOCTYPE html>
<html lang="en">
<head>
<meta charset="utf-8">
<title>Brightwave Business Cards</title>
<link href="https://fonts.googleapis.com/css2?family=Oswald:wght@300;400&family=Playfair+Display:wght@400;500&display=swap" rel="stylesheet">
<style>
  :root {
    --backdrop: #d6d6d6;
    --card: #ffffff;
    --brand-blue: #1b7fb4;
    --teal: #1aa3bf;
    --navy: #14344f;
    --text-grey: #4a4a4a;
    --white: #ffffff;
  }
  * { margin: 0; padding: 0; box-sizing: border-box; }
  html, body {
    width: 1200px; height: 800px; overflow: hidden;
    background: var(--backdrop);
  }
  .canvas { position: relative; width: 1200px; height: 800px; }
  .card {
    position: absolute; top: 283px;
    width: 430px; height: 238px;
    background: var(--card); overflow: hidden;
  }
  .card--contact { left: 110px; }
  .card--company { left: 638px; }

  .decor-panel {
    position: absolute;
    background: linear-gradient(100deg, var(--teal) 0%, var(--navy) 45%, var(--navy) 100%);
  }
  .decor-panel--contact {
    left: 205px; top: -20px; width: 260px; height: 280px;
    border-top-left-radius: 100% 100%;
  }
  .decor-panel--corner-top {
    right: -40px; top: -40px; width: 90px; height: 190px;
    border-bottom-left-radius: 100% 100%;
    background: linear-gradient(90deg, var(--teal), var(--navy));
  }
  .decor-panel--corner-bottom {
    left: -40px; bottom: -40px; width: 95px; height: 170px;
    border-top-right-radius: 100% 100%;
    background: linear-gradient(270deg, var(--teal), var(--navy));
  }

  .wordmark {
    position: absolute;
    font-family: "Playfair Display", serif;
    font-weight: 500; color: var(--brand-blue);
    letter-spacing: 1.5px; white-space: nowrap;
  }
  .card--contact .wordmark { left: 24px; top: 34px; font-size: 13.5px; }
  .card--company .wordmark {
    left: 0; right: 0; top: 104px; text-align: center; font-size: 22px; letter-spacing: 2px;
  }

  .contact-list {
    position: absolute; left: 25px; top: 128px; list-style: none;
    font-family: "Playfair Display", serif; color: var(--text-grey);
  }
  .contact-list__item { display: flex; align-items: flex-start; gap: 6px; font-size: 11.5px; line-height: 1.2; margin-bottom: 8px; }
  .contact-list__icon { width: 9px; height: 9px; margin-top: 2px; flex: none; }
  .contact-list__name { font-size: 13px; display: block; }
  .contact-list__title { font-size: 11px; display: block; }

  .quote {
    position: absolute; right: 20px; top: 175px; text-align: right;
    font-family: "Oswald", sans-serif; font-weight: 300;
    color: var(--white); text-transform: uppercase; font-size: 7.5px; letter-spacing: 0.1px;
  }
  .quote__by { display: block; margin-top: 9px; }

  .address-pill {
    position: absolute; left: 80px; top: 192px; width: 272px; height: 18px;
    border-radius: 9px; background: var(--teal); color: var(--white);
    font-family: "Playfair Display", serif; font-size: 11.5px;
    text-align: center; line-height: 18px; white-space: nowrap;
  }
</style>
</head>
<body>
<main class="canvas">

  <section class="card card--contact">
    <div class="decor-panel decor-panel--contact" role="img" aria-label="Decorative layered teal and navy wave artwork"></div>

    <div class="wordmark">BRIGHTWAVE CHIEF</div>

    <ul class="contact-list">
      <li class="contact-list__item">
        <svg class="contact-list__icon" viewBox="0 0 10 10" aria-hidden="true"><circle cx="5" cy="5" r="5" fill="var(--brand-blue)"/><circle cx="5" cy="4" r="1.6" fill="#fff"/><path d="M2.6,7.6 C3,6 7,6 7.4,7.6 Z" fill="#fff"/></svg>
        <span><span class="contact-list__name">Dorian Pelley</span><span class="contact-list__title">CEO</span></span>
      </li>
      <li class="contact-list__item">
        <svg class="contact-list__icon" viewBox="0 0 10 10" aria-hidden="true"><circle cx="5" cy="5" r="5" fill="var(--brand-blue)"/><path d="M3.2,2.6 L4.2,2.4 L4.6,3.8 L4,4.3 C4.3,5 4.9,5.6 5.7,6 L6.2,5.4 L7.6,5.8 L7.4,6.8 C5.2,7 3,4.8 3.2,2.6 Z" fill="#fff"/></svg>
        <span>619-555-0148</span>
      </li>
      <li class="contact-list__item">
        <svg class="contact-list__icon" viewBox="0 0 10 10" aria-hidden="true"><circle cx="5" cy="5" r="5" fill="var(--brand-blue)"/><rect x="2.6" y="3.4" width="4.8" height="3.4" fill="#fff"/><path d="M2.6,3.4 L5,5.3 L7.4,3.4" stroke="var(--brand-blue)" stroke-width="0.6" fill="none"/></svg>
        <span>Dorian@BrightwaveChief.com</span>
      </li>
    </ul>

    <p class="quote">“The fastest way to success is to take action”<span class="quote__by">— Dorian Pelley, Brightwave Chief</span></p>
  </section>

  <section class="card card--company">
    <div class="decor-panel decor-panel--corner-top" role="img" aria-label="Decorative teal and navy wave artwork in the top corner"></div>
    <div class="decor-panel decor-panel--corner-bottom" role="img" aria-label="Decorative teal and navy wave artwork in the bottom corner"></div>

    <div class="wordmark">BRIGHTWAVE OUTREACH</div>

    <p class="address-pill">482 N. Elmwood 3rd Floor San Diego CA 92101</p>
  </section>

</main>
</body>
</html>
```